Business and Success Coaching Business Card

Need a business card for my coaching business. I coach small businesses, career professionals and, individuals wanting to unlock their human potential and achieve excellence. At the heart of our methodology is the Shaping Purposeful Action Routines Knowingly (SPARK) approach to formulate empowerment, create principles for success and setting achievable outcomes. I would like something that incorporates our new logo, something clean and sharp with a solid darker, but complementary background, color on the card front. The back should be white where there will be room for three questions

Target Market(s)

People looking to advance and improve themselves through a success coach

Industry/Entity Type

Life Coaching

Contact Information for Business Card

Contact information on card.
Business name on front of card
Questions on back

Font styles to use
Other font styles liked:
• Century Gothic or other Serif style fonts that look similar to Century Gothic

Colors

Designer to choose colors to be used in the design.

Requirements
Must have
• Logo on front of card
• Business name - The Steady Forge
• Contact name - Ted Harlow
• Address - Box 4619, Maple Ridge, OR 97891-4619
• Phone number - 303-555-0147
• Email address - harlow.ted@thesteadyforge.example
• Certifications - CSC, CCHt, PTT, PNLP
• Back of card
• Three questions on the back of the card:
• If you were at your best, what would you do right now?
• What is the decision you have been avoiding?
• What's one action you could take in the next 10 minutes?
Nice to have
• I would like to see a solid color on the front of the card that compliments the logo.
• Back should be white, or could be contrasting, but need to have the three questions.

```html
<!DOCTYPE html>
<html lang="en">
<head>
<meta charset="utf-8">
<title>The Steady Forge – Business Card</title>
<link rel="stylesheet" href="https://fonts.googleapis.com/css2?family=Open+Sans:wght@400;600;700&family=Arimo:wght@400;700&display=swap">
<style>
  :root {
    --navy: #233a73;
    --navy-deep: #1d3168;
    --accent: #3d6fc6;
    --pale-blue: #c9d6ee;
    --white: #ffffff;
    --ink: #22397a;
    --stage: #2b2b2d;
  }
  * { box-sizing: border-box; margin: 0; padding: 0; }
  html, body { width: 1200px; height: 880px; overflow: hidden; }
  body {
    background: var(--stage);
    display: flex;
    flex-direction: column;
    align-items: center;
    justify-content: center;
    gap: 24px;
  }
  .card {
    width: 700px;
    height: 400px;
    border-radius: 22px;
    position: relative;
    overflow: hidden;
    box-shadow: 0 8px 24px rgba(0,0,0,.45);
  }

  /* Front: brand side */
  .card-front {
    background: var(--navy);
    color: var(--white);
    font-family: "Open Sans", sans-serif;
    display: flex;
    flex-direction: column;
    align-items: center;
    justify-content: center;
    text-align: center;
  }
  .brand-name {
    font-size: 50px;
    font-weight: 700;
    letter-spacing: .5px;
    line-height: 1;
  }
  .brand-tagline {
    font-size: 24px;
    font-weight: 400;
    color: var(--pale-blue);
    margin-top: 4px;
    letter-spacing: .5px;
  }
  .questions {
    list-style: none;
    margin-top: 38px;
    font-size: 17px;
    line-height: 1.45;
  }

  /* Back: contact side */
  .card-back {
    background: var(--white);
    font-family: "Arimo", sans-serif;
    color: var(--ink);
  }
  .logo-block {
    position: absolute;
    left: 40px;
    top: 120px;
    width: 300px;
    display: flex;
    flex-direction: column;
    align-items: center;
    text-align: center;
  }
  .logo-dot {
    width: 62px;
    height: 62px;
    border-radius: 50%;
    background: var(--navy);
    margin-bottom: 14px;
  }
  .logo-name {
    font-family: "Open Sans", sans-serif;
    font-weight: 700;
    font-size: 34px;
    color: var(--navy);
    line-height: 1;
  }
  .logo-tagline {
    font-family: "Open Sans", sans-serif;
    font-size: 15px;
    color: var(--pale-blue);
    margin-top: 4px;
  }
  .divider {
    position: absolute;
    left: 360px;
    top: 60px;
    width: 1px;
    height: 200px;
    background: var(--accent);
  }
  .contact {
    position: absolute;
    left: 384px;
    top: 64px;
  }
  .contact-name {
    font-family: "Open Sans", sans-serif;
    font-weight: 700;
    font-size: 26px;
    color: var(--navy);
  }
  .contact-address {
    font-size: 17px;
    line-height: 1.3;
    margin-top: 12px;
  }
  .contact-lines { list-style: none; margin-top: 14px; font-size: 16px; }
  .contact-lines li { display: flex; align-items: center; gap: 8px; margin-bottom: 6px; }
  .contact-icon { width: 18px; height: 18px; flex: none; }
  .cert-band {
    position: absolute;
    left: 0; right: 0;
    bottom: 34px;
    height: 72px;
    background: var(--navy-deep);
    color: var(--white);
    font-size: 22px;
    letter-spacing: 2px;
    display: flex;
    align-items: center;
    justify-content: center;
  }
  .cert-rule {
    position: absolute;
    left: 0; right: 0;
    bottom: 26px;
    height: 4px;
    background: var(--pale-blue);
  }
</style>
</head>
<body>

<section class="card card-front" aria-label="Card front">
  <h1 class="brand-name">The Steady Forge</h1>
  <p class="brand-tagline">Build your next stride</p>
  <ul class="questions">
    <li>If you were at your best, what would you do right now?</li>
    <li>What is the decision you have been avoiding?</li>
    <li>What's one action you could take in the next 10 minutes?</li>
  </ul>
</section>

<section class="card card-back" aria-label="Card back">
  <div class="logo-block">
    <span class="logo-dot"></span>
    <span class="logo-name">The Steady Forge</span>
    <span class="logo-tagline">Build your next stride</span>
  </div>

  <span class="divider"></span>

  <div class="contact">
    <p class="contact-name">Ted Harlow</p>
    <p class="contact-address">Box 4619, Maple Ridge<br>OR 97891-4619</p>
    <ul class="contact-lines">
      <li>
        <svg class="contact-icon" viewBox="0 0 20 20" aria-hidden="true">
          <circle cx="10" cy="10" r="10" fill="var(--accent)"/>
          <path d="M7 5.5l2 2-1 1.3c.6 1.3 1.6 2.3 2.9 2.9l1.3-1 2 2-1.3 1.6C9.5 14 6 10.5 5.6 6.7z" fill="#fff"/>
        </svg>
        303-555-0147
      </li>
      <li>
        <svg class="contact-icon" viewBox="0 0 20 20" aria-hidden="true">
          <circle cx="10" cy="10" r="10" fill="var(--accent)"/>
          <rect x="5" y="6.5" width="10" height="7" rx="1" fill="#fff"/>
          <path d="M5.4 7l4.6 3.6L14.6 7" fill="none" stroke="var(--accent)" stroke-width="1.2"/>
        </svg>
        harlow.ted@thesteadyforge.example
      </li>
    </ul>
  </div>

  <div class="cert-band">Certifications - CSC, CCHt, PTT, PNLP</div>
  <span class="cert-rule"></span>
</section>

</body>
</html>
```